Fitness company needs new web design

We are looking to get our current site design improved to a newer design to better match our logo and features.

Current Site:
brinovamotion.com

* We would like the site to be modern/simple.
* The site will need to have the ability to take payments via stripe.
* We would like a "shop" page, as we will be selling supplements. Possible linkup with Shopify.
* The main landing page should flow in a way to sell our personal training & diet services. We would like the user to have to input their info (like we currently have) before placing an order.

We like how this site is put together: lumarifit.com

We use this service for our mobile app that our clients get to use when they signup: trelvacoach.net

If you have any questions please message use before starting your design.

Target Market(s)

Weight Loss, Fitness, Sports Athletes

Industry/Entity Type

Fitness

Coding

Coded - Design and coding required

Number of Pages Required

5+ page

Colors

Designer to choose colors to be used in the design.

Requirements
Must have
• Menu Tabs:
• - Programs
• - We offer 3 programs (see below for complete details)
• * Basic
• * Premium
• * Elite
• - Supplements
• - We currently have 2 supplements (see attached labels)
• * Vima Rise
• * Vima Blaze
• - About
• - FAQ
• - Contact
• - Book Appointment (calendly.com)
• Program Breakdown:
• Basic: Price $99/month
• - One 30 Minute In-Person or Phone Consultation
• - Unlimited in-app text support
• - Basic Nutrition Education
• - 30 Day Meal Plan
• Premium: Price $149/month
• - Two 30 Minute In-Person or Phone Consultations
• - Unlimited In-App Messaging Support
• - Customized Strength Training Program
• - Each Exercise Demonstrated in HD Videos
• - Personalized Cardio Program
• - Personalized Nutrition Coaching & Meal Plans
• Elite: Price $249/month
• - Weekly 30 Minute In-Person or Phone Consultation
• - Weekly Customized Strength Training Program
• - Weekly Customized Cardio Training Program
• - Bi-Weekly Nutrition Coaching & Meal Plans
Nice to have
• Click through form that collects clients information (like we have on our current site brinovamotion.com

```html
<!DOCTYPE html>
<html lang="en">
<head>
<meta charset="utf-8">
<title>Brinova Motion – Personal Coaching</title>
<link href="https://fonts.googleapis.com/css2?family=Oswald:wght@400;500;600;700&family=Roboto:wght@300;400;500;700&family=Playfair+Display:ital,wght@1,700&display=swap" rel="stylesheet">
<style>
:root{
  --red:#c23a2c;
  --red-dark:#a92f23;
  --purple:#8c42a6;
  --purple-dark:#6f2f87;
  --gold:#e9a900;
  --yellow:#e3c548;
  --yellow-pale:#f3f08a;
  --ink:#1e1e1e;
  --text:#555;
  --muted:#8a8a8a;
  --grey-row:#ebebeb;
  --beige-row:#f8efd8;
  --footer:#242424;
  --footer-line:#3a3a3a;
  --white:#fff;
}
*{box-sizing:border-box;margin:0;padding:0}
html,body{width:1200px;height:3750px;overflow:hidden}
body{position:relative;font-family:'Roboto',Arial,sans-serif;color:var(--text);background:var(--white)}

/* top bar */
.topbar{position:absolute;top:0;left:0;width:1200px;height:70px;background:var(--white)}
.brand-block{position:absolute;left:0;top:0;width:410px;height:70px;background:linear-gradient(90deg,#3a3a3a,#5a5a5a);clip-path:polygon(0 0,100% 0,91% 100%,0 100%);display:flex;align-items:center;padding-left:160px;gap:10px}
.brand-mark{width:24px;height:24px;background:var(--yellow)}
.brand-name{font-family:'Oswald',sans-serif;font-weight:500;font-size:22px;color:var(--white);letter-spacing:1px}
.contact-item{position:absolute;top:16px;display:flex;align-items:center;gap:12px}
.contact-item svg{width:34px;height:34px}
.contact-item strong{display:block;font-size:14px;font-weight:400;color:#333}
.contact-item span{display:block;font-size:10px;color:var(--muted);margin-top:2px}

/* nav */
.nav{position:absolute;top:70px;left:0;width:1200px;height:48px;background:var(--red)}
.nav a{position:absolute;top:17px;font-family:'Oswald',sans-serif;font-size:13px;color:var(--white);text-decoration:none;letter-spacing:.5px}
.social{position:absolute;top:13px;left:900px;display:flex;gap:15px}
.social span{width:22px;height:22px;border:1px solid rgba(255,255,255,.7);background:rgba(255,255,255,.12)}

/* hero */
.hero-photo{position:absolute;top:118px;left:0;width:1200px;height:570px;background:linear-gradient(100deg,#2d2620 0%,#5b4a3d 35%,#8f7766 58%,#4a3c33 80%,#2a2420 100%)}
.hero-kicker{position:absolute;top:288px;left:162px;font-family:'Oswald',sans-serif;font-weight:400;font-size:26px;color:var(--white);text-transform:uppercase}
.hero-title{position:absolute;top:318px;left:162px;font-family:'Oswald',sans-serif;font-weight:600;font-size:38px;color:var(--white);text-transform:uppercase}
.hero-text{position:absolute;top:368px;left:162px;width:420px;font-size:13px;line-height:16px;color:#f1f1f1}
.btn-outline{position:absolute;top:402px;left:162px;height:40px;padding:0 14px;border:2px solid var(--white);font-family:'Oswald',sans-serif;font-size:14px;color:var(--white);line-height:36px;text-transform:uppercase}

/* help box */
.help{position:absolute;top:555px;left:162px;width:876px;height:403px;background:var(--purple);text-align:center;color:var(--white)}
.help h2{margin-top:35px;font-family:'Oswald',sans-serif;font-weight:600;font-size:28px;text-transform:uppercase;color:var(--white)}
.help .note{margin-top:16px;font-size:11px;color:#eadff0}
.help .rule{margin:14px auto 0;width:760px;height:1px;background:rgba(255,255,255,.3)}
.services{display:flex;justify-content:space-between;padding:0 40px;margin-top:25px}
.service{width:250px;position:relative}
.service+.service:before{content:"";position:absolute;left:-18px;top:20px;width:1px;height:180px;background:rgba(255,255,255,.3)}
.service-icon{width:110px;height:110px;border-radius:50%;background:var(--purple-dark);margin:0 auto;border:2px solid rgba(255,255,255,.25);display:flex;align-items:center;justify-content:center}
.service h3{margin-top:24px;font-family:'Oswald',sans-serif;font-weight:500;font-size:14px;text-transform:uppercase}
.service p{margin-top:8px;font-size:11px;line-height:15px;color:#f0e6f4}

/* discover */
.discover-title{position:absolute;top:1005px;left:162px;font-family:'Oswald',sans-serif;font-weight:700;font-size:32px;color:var(--ink)}
.discover-sub{position:absolute;top:1043px;left:162px;font-family:'Oswald',sans-serif;font-weight:400;font-size:26px;color:var(--ink);text-transform:uppercase}
.discover-lead{position:absolute;top:1085px;left:162px;font-size:18px;color:#9a9a9a;font-weight:300}
.discover-text{position:absolute;top:1123px;left:162px;width:470px;font-size:13px;line-height:21px;color:var(--muted)}
.btn-dark-outline{position:absolute;top:1238px;left:162px;width:106px;height:37px;border:2px solid #333;font-family:'Oswald',sans-serif;font-size:12px;color:#333;display:flex;align-items:center;justify-content:center;gap:6px}
.discover-art{position:absolute;top:985px;left:685px;width:345px;height:345px}

/* success */
.success{position:absolute;top:1338px;left:0;width:568px;height:417px;background:var(--red);color:var(--white)}
.success h2{position:absolute;top:28px;left:162px;font-family:'Playfair Display',Georgia,serif;font-style:italic;font-weight:700;font-size:25px}
.success .intro{position:absolute;top:68px;left:162px;width:330px;font-size:12px;line-height:16px;font-weight:500}
.perk{position:absolute;left:162px;width:390px;display:flex;gap:18px}
.perk-icon{width:42px;height:42px;border-radius:50%;background:var(--red-dark);border:1px solid rgba(255,255,255,.35);flex:none;display:flex;align-items:center;justify-content:center}
.perk h3{font-size:14px;font-weight:500;margin-top:2px}
.perk p{font-size:10px;line-height:14px;color:#f4d9d5;margin-top:4px}
.success-photo{position:absolute;top:1338px;left:568px;width:632px;height:417px;background:linear-gradient(110deg,#d9c3a8 0%,#c8a383 35%,#b98b6a 55%,#e4d2be 100%)}

/* programs */
.programs-title{position:absolute;top:1820px;left:0;width:1200px;text-align:center;font-family:'Oswald',sans-serif;font-weight:500;font-size:32px;color:var(--ink)}
.diamond{position:absolute;top:1870px;left:595px;width:10px;height:10px;background:var(--ink);transform:rotate(45deg)}
.programs-text{position:absolute;top:1900px;left:270px;width:660px;text-align:center;font-size:11px;line-height:16px;color:var(--text)}
.plan{position:absolute;text-align:center}
.plan-head{display:flex;align-items:center;justify-content:center;font-family:'Oswald',sans-serif;font-weight:500;font-size:28px;color:var(--white);text-transform:uppercase}
.plan-price{display:flex;align-items:center;justify-content:center;font-size:19px;color:#222}
.plan-row{display:flex;align-items:center;justify-content:center;font-size:12px;color:#333;padding:0 8px;white-space:nowrap}
.plan-elite .plan-row{font-size:11.5px}
.grey{background:var(--grey-row)}
.beige{background:var(--beige-row)}
.white{background:var(--white)}
.pill{display:inline-flex;align-items:center;gap:12px;height:46px;padding:0 8px 0 24px;border-radius:23px;font-family:'Oswald',sans-serif;font-weight:500;font-size:16px;color:var(--white);text-transform:uppercase}
.pill .cart{width:32px;height:32px;border-radius:50%;background:var(--white);display:flex;align-items:center;justify-content:center}
.plan-basic{top:1988px;left:162px;width:288px}
.plan-premium{top:1963px;left:445px;width:310px;background:var(--white);box-shadow:0 6px 18px rgba(0,0,0,.25);z-index:2}
.plan-elite{top:1988px;left:755px;width:283px}

/* newsletter */
.newsletter{position:absolute;top:2613px;left:0;width:1200px;height:262px;background:linear-gradient(90deg,#dfbf40,#e8cd5a 50%,#dfbf40)}
.newsletter h2{position:absolute;top:37px;left:0;width:1200px;text-align:center;font-family:'Oswald',sans-serif;font-weight:600;font-size:34px;color:var(--ink)}
.newsletter p{position:absolute;top:90px;left:250px;width:700px;text-align:center;font-size:12px;line-height:18px;color:#333}
.field{position:absolute;top:170px;height:35px;background:#f3f3f3;display:flex;align-items:center;gap:8px;padding-left:12px;font-size:11px;color:#777}
.btn-subscribe{position:absolute;top:170px;left:912px;width:126px;height:35px;background:var(--red);color:var(--white);font-family:'Oswald',sans-serif;font-size:13px;display:flex;align-items:center;justify-content:center}

/* guarantee */
.badge{position:absolute;top:2905px;left:520px;width:160px;height:160px;border-radius:50%;background:radial-gradient(circle at 50% 45%,#c9302f 0%,#b9262a 65%,#a31f24 100%)}
.guarantee-title{position:absolute;top:3098px;left:0;width:1200px;text-align:center;font-family:'Oswald',sans-serif;font-weight:600;font-size:28px;color:var(--ink)}
.guarantee-text{position:absolute;top:3152px;left:300px;width:600px;text-align:center;font-size:11px;line-height:18px;color:#333;text-transform:uppercase}
.btn-purple{position:absolute;top:3220px;left:482px;width:243px;height:50px;background:var(--purple);color:var(--white);font-family:'Oswald',sans-serif;font-size:16px;display:flex;align-items:center;justify-content:center;text-transform:uppercase}

/* footer */
.footer{position:absolute;top:3338px;left:0;width:1200px;height:357px;background:var(--footer);color:#bbb}
.footer h4{position:absolute;top:45px;font-family:'Oswald',sans-serif;font-weight:500;font-size:15px;color:var(--white);text-transform:uppercase}
.about-text{position:absolute;top:82px;left:162px;width:210px;font-size:11px;line-height:16px;color:#999}
.info{position:absolute;left:162px;width:220px;font-size:11px;line-height:15px;color:#999}
.info b{display:flex;align-items:center;gap:6px;font-family:'Oswald',sans-serif;font-weight:500;font-size:13px;color:var(--white);margin-bottom:3px}
.news{position:absolute;left:442px;width:260px;height:70px}
.news-date{position:absolute;left:0;top:0;width:50px;height:50px;border:1px solid #555;text-align:center;color:var(--white)}
.news-date strong{display:block;font-family:'Oswald',sans-serif;font-size:18px;font-weight:400;margin-top:4px}
.news-date span{display:block;font-size:9px}
.news-more{position:absolute;top:55px;left:0;font-size:8px;color:#888}
.news-body{position:absolute;left:62px;top:0;width:200px;font-size:10px;line-height:13px}
.news-body .t{color:#ddd}
.news-body .m{color:#888;font-size:8px}
.news-body .loc{color:#aaa;font-size:9px;display:flex;align-items:center;gap:4px}
.news-body .loc:before{content:"";width:5px;height:5px;background:var(--red);border-radius:50%}
.news-line{position:absolute;left:442px;width:250px;height:1px;background:var(--footer-line)}
.form-field{position:absolute;left:755px;width:283px;height:32px;border:1px solid #444;background:#2c2c2c;font-size:10px;color:#888;padding:9px 10px}
.btn-submit{position:absolute;top:280px;left:755px;width:80px;height:32px;background:var(--gold);color:var(--white);font-family:'Oswald',sans-serif;font-size:13px;display:flex;align-items:center;justify-content:center}
.copyright{position:absolute;top:3695px;left:0;width:1200px;height:55px;background:var(--red);color:var(--white);font-size:12px;display:flex;align-items:center;justify-content:center}
</style>
</head>
<body>

<header class="topbar">
  <div class="brand-block"><span class="brand-mark"></span><span class="brand-name">BRINOVA MOTION</span></div>
  <div class="contact-item" style="left:455px">
    <svg viewBox="0 0 34 34"><circle cx="17" cy="17" r="15" fill="none" stroke="#c23a2c" stroke-width="1.5"/><path d="M17 8v9l6 4" fill="none" stroke="#c23a2c" stroke-width="1.8"/></svg>
    <div><strong>Monday - Friday 08:00-19:00</strong><span>Saturday and Sunday - CLOSED</span></div>
  </div>
  <div class="contact-item" style="left:710px">
    <svg viewBox="0 0 34 34"><path d="M10 6l5 5-3 4c2 4 4 6 8 8l4-3 5 5-4 4C14 28 6 20 6 10z" fill="none" stroke="#c23a2c" stroke-width="1.6"/></svg>
    <div><strong>+0800 4417 2093</strong><span>info@brinovamotion.com</span></div>
  </div>
  <div class="contact-item" style="left:925px">
    <svg viewBox="0 0 34 34"><path d="M17 31s-9-10-9-17a9 9 0 0 1 18 0c0 7-9 17-9 17z" fill="none" stroke="#c23a2c" stroke-width="1.6"/><circle cx="17" cy="14" r="3.5" fill="none" stroke="#c23a2c" stroke-width="1.6"/></svg>
    <div><strong>Lorem Ipsum</strong><span>New York, NY 345</span></div>
  </div>
</header>

<nav class="nav">
  <a style="left:162px">PROGRAMS</a>
  <a style="left:255px">SUPPLEMENTS</a>
  <a style="left:363px">ABOUT</a>
  <a style="left:430px">FAQ</a>
  <a style="left:488px">CONTACT</a>
  <a style="left:570px">BOOK APPOINTMENT</a>
  <div class="social"><span></span><span></span><span></span><span></span></div>
</nav>

<div class="hero-photo" role="img" aria-label="Smiling woman lifting a barbell in a busy gym with other athletes training behind her"></div>
<p class="hero-kicker">Stop dieting and start</p>
<h1 class="hero-title">Losing more weight faster!</h1>
<p class="hero-text">Brinova Motion is a 100% custom online personal coaching program for those looking to burn fat while building a lean athletic body.</p>
<div class="btn-outline">Get my customized plan</div>

<section class="help">
  <h2>We help you lose weight and keep it off!*</h2>
  <p class="note">Results vary depending on starting point, goals, and effort</p>
  <div class="rule"></div>
  <div class="services">
    <div class="service">
      <div class="service-icon">
        <svg width="52" height="56" viewBox="0 0 52 56" fill="none" stroke="#fff" stroke-width="3" aria-hidden="true"><rect x="8" y="8" width="36" height="44" rx="3"/><rect x="18" y="3" width="16" height="9" rx="2" fill="#6f2f87"/><path d="M16 24l4 4 8-8M16 40h20M16 33h20"/></svg>
      </div>
      <h3>Custom meal plans</h3>
      <p>Aenean lacinia bibendum nulla sed consectetur. Faucibus dolor auctor.Donec id elit non mi porta gravida at eget metus.</p>
    </div>
    <div class="service">
      <div class="service-icon">
        <svg width="60" height="30" viewBox="0 0 60 30" fill="#fff" aria-hidden="true"><rect x="2" y="9" width="6" height="12" rx="1"/><rect x="9" y="3" width="8" height="24" rx="1.5"/><rect x="17" y="13" width="26" height="4"/><rect x="43" y="3" width="8" height="24" rx="1.5"/><rect x="52" y="9" width="6" height="12" rx="1"/></svg>
      </div>
      <h3>Custom training plans</h3>
      <p>Aenean lacinia bibendum nulla sed consectetur. Faucibus dolor auctor.Donec id elit non mi porta gravida at eget metus.</p>
    </div>
    <div class="service">
      <div class="service-icon">
        <svg width="54" height="48" viewBox="0 0 54 48" fill="none" stroke="#fff" stroke-width="3" aria-hidden="true"><path d="M4 6h30v20H16l-8 7v-7H4z"/><path d="M38 16h12v18h-4v7l-8-7H22v-4"/></svg>
      </div>
      <h3>One on one coaching</h3>
      <p>Aenean lacinia bibendum nulla sed consectetur. Faucibus dolor auctor.Donec id elit non mi porta gravida at eget metus.</p>
    </div>
  </div>
</section>

<h2 class="discover-title">DISCOVER</h2>
<p class="discover-sub">How you can burn fat</p>
<p class="discover-lead">and build a lean body at the same time!</p>
<p class="discover-text">muscles energy stores, ketosis preserves your body's ability to retain glycogen during physical activities while increasing fat oxidation. Since your body is using it's nearly unlimited fat stores for fuel, it mobilizes the fat for fuel and preserves precious muscle mass.</p>
<div class="btn-dark-outline">READ MORE
  <svg width="12" height="12" viewBox="0 0 12 12"><circle cx="6" cy="6" r="6" fill="#333"/><path d="M5 3l3 3-3 3" fill="none" stroke="#fff" stroke-width="1.5"/></svg>
</div>
<svg class="discover-art" viewBox="0 0 345 345">
  <circle cx="95" cy="90" r="88" fill="#f4f08c"/>
  <circle cx="250" cy="190" r="92" fill="#f4f08c"/>
  <circle cx="120" cy="265" r="78" fill="#f4f08c"/>
  <g role="img" aria-label="Athlete training with a rope in the gym"><circle cx="95" cy="90" r="64" fill="#6d6a68" stroke="#fff" stroke-width="5"/></g>
  <g role="img" aria-label="Trainer helping a client stretch"><circle cx="250" cy="190" r="66" fill="#b7463a" stroke="#fff" stroke-width="5"/></g>
  <g role="img" aria-label="Woman running along the seaside"><circle cx="120" cy="265" r="58" fill="#8fb7d6" stroke="#fff" stroke-width="5"/></g>
</svg>

<section class="success">
  <h2>Your Success Is Our Success</h2>
  <p class="intro">Don't be just another sale, join a community of like-minded people that want to see you succeed!</p>
  <div class="perk" style="top:132px">
    <div class="perk-icon"><svg width="22" height="22" viewBox="0 0 22 22" fill="#fff"><circle cx="11" cy="7" r="3"/><circle cx="4.5" cy="9" r="2.2"/><circle cx="17.5" cy="9" r="2.2"/><path d="M5 18c0-4 3-6 6-6s6 2 6 6z"/></svg></div>
    <div><h3>Private Online Community</h3><p>Lorem Ipsum is simply dummy text of the printing and typesetting industry. Lorem Ipsum has been the industry's standard...</p></div>
  </div>
  <div class="perk" style="top:207px">
    <div class="perk-icon"><svg width="20" height="20" viewBox="0 0 20 20" fill="none" stroke="#fff" stroke-width="1.6"><rect x="3" y="4" width="14" height="13" rx="1"/><path d="M3 8h14M7 2v4M13 2v4"/></svg></div>
    <div><h3>Weekly Accountability Calls</h3><p>Lorem Ipsum is simply dummy text of the printing and typesetting industry. Lorem Ipsum has been the industry's standard...</p></div>
  </div>
  <div class="perk" style="top:280px">
    <div class="perk-icon"><svg width="20" height="20" viewBox="0 0 20 20" fill="none" stroke="#fff" stroke-width="1.6"><rect x="2" y="5" width="16" height="11"/><path d="M2 5l8 6 8-6"/></svg></div>
    <div><h3>Unlimited Text &amp; Email Support</h3><p>Lorem Ipsum is simply dummy text of the printing and typesetting industry. Lorem Ipsum has been the industry's standard...</p></div>
  </div>
  <div class="perk" style="top:352px">
    <div class="perk-icon"><svg width="20" height="20" viewBox="0 0 20 20" fill="#fff"><circle cx="10" cy="6" r="3.5"/><path d="M3 18c0-5 3.5-7 7-7s7 2 7 7z"/></svg></div>
    <div><h3>Member Portal Access</h3><p>Lorem Ipsum is simply dummy text of the printing and typesetting industry. Lorem Ipsum has been the industry's standard...</p></div>
  </div>
</section>
<div class="success-photo" role="img" aria-label="Woman in a sports top running outdoors in warm sunlight"></div>

<h2 class="programs-title">PROGRAM BREAKDOWN</h2>
<div class="diamond"></div>
<p class="programs-text">Lorem ipsum dolor sit amet, consectetur adipiscing elit. Nunc congue urna et diam eleifend, eu faucibus est eleifend. Quisque a dui quis ante porta ultrices. Lorem ipsum dolor sit amet, consectetur adipiscing</p>

<div class="plan plan-basic">
  <div class="plan-head" style="height:75px;background:var(--red)">Basic</div>
  <div class="plan-price grey" style="height:62px">Price $99/month</div>
  <div class="plan-row white" style="height:62px">One 30 Minute In-Person or Phone Consultation</div>
  <div class="plan-row grey" style="height:62px">Unlimited in-app text support</div>
  <div class="plan-row white" style="height:62px">Basic Nutrition Education</div>
  <div class="grey" style="height:150px;padding-top:22px">
    <div style="font-size:12px;color:#333">30 Day Meal Plan</div>
    <div class="pill" style="background:var(--red);margin-top:22px">Order now
      <span class="cart"><svg width="16" height="16" viewBox="0 0 16 16" fill="#c23a2c"><path d="M1 2h3l2 8h7l2-6H5"/><circle cx="7" cy="13" r="1.5"/><circle cx="12" cy="13" r="1.5"/></svg></span>
    </div>
  </div>
</div>

<div class="plan plan-premium">
  <div class="plan-head" style="height:82px;background:var(--gold)">Premium</div>
  <div class="plan-price white" style="height:67px">Price $149/month</div>
  <div class="plan-row beige" style="height:57px">Two 30 Minute In-Person or Phone Consultations</div>
  <div class="plan-row white" style="height:57px">Unlimited In-App Messaging Support</div>
  <div class="plan-row beige" style="height:57px">Customized Strength Training Program</div>
  <div class="plan-row white" style="height:57px">Each Exercise Demonstrated in HD Videos</div>
  <div class="plan-row beige" style="height:57px">Personalized Cardio Program</div>
  <div class="plan-row white" style="height:57px">Personalized Nutrition Coaching &amp; Meal Plans</div>
  <div class="white" style="height:80px;padding-top:14px">
    <div class="pill" style="background:#1b1b1b;height:52px;border-radius:26px;padding-left:40px;gap:24px">Shop now
      <span class="cart"><svg width="16" height="16" viewBox="0 0 16 16" fill="#1b1b1b"><path d="M1 2h3l2 8h7l2-6H5"/><circle cx="7" cy="13" r="1.5"/><circle cx="12" cy="13" r="1.5"/></svg></span>
    </div>
  </div>
</div>

<div class="plan plan-elite">
  <div class="plan-head" style="height:75px;background:var(--purple)">Elite</div>
  <div class="plan-price grey" style="height:62px">Price $249/month</div>
  <div class="plan-row white" style="height:52px">Weekly 30 Minute In-Person or Phone Consultation</div>
  <div class="plan-row grey" style="height:52px">Unlimited In-App Messaging Support</div>
  <div class="plan-row white" style="height:52px">Weekly Customized Strength Training Program</div>
  <div class="plan-row grey" style="height:52px">Each Exercise Demonstrated in HD Videos</div>
  <div class="plan-row white" style="height:52px">Weekly Customized Cardio Training Program</div>
  <div class="grey" style="height:76px;padding-top:14px">
    <div class="pill" style="background:var(--purple)">Shop now
      <span class="cart"><svg width="16" height="16" viewBox="0 0 16 16" fill="#8c42a6"><path d="M1 2h3l2 8h7l2-6H5"/><circle cx="7" cy="13" r="1.5"/><circle cx="12" cy="13" r="1.5"/></svg></span>
    </div>
  </div>
</div>

<section class="newsletter">
  <h2>SIGN UP FOR NEWSLETTER</h2>
  <p>Lorem Ipsum is simply dummy text of the printing and typesetting industry. Lorem Ipsum has been the industry's standard dummy text ever since, when an unknown printer took.</p>
  <div class="field" style="left:162px;width:363px"><svg width="11" height="11" viewBox="0 0 12 12" fill="#666"><circle cx="6" cy="3.5" r="2.5"/><path d="M1 12c0-4 2.5-5 5-5s5 1 5 5z"/></svg>Enter Your Name</div>
  <div class="field" style="left:538px;width:362px"><svg width="12" height="10" viewBox="0 0 12 10" fill="none" stroke="#666"><rect x=".5" y=".5" width="11" height="9"/><path d="M.5 .5l5.5 5 5.5-5"/></svg>Enter Your Email</div>
  <div class="btn-subscribe">SUBSCRIBE NOW!</div>
</section>

<div class="badge" role="img" aria-label="30 day money back guarantee seal"></div>
<h2 class="guarantee-title">30 DAY MONEY BACK GUARANTEE</h2>
<p class="guarantee-text">If you do not experience the results you should by the efforts you put in, we will refund 100% of the cost of the program. So what do you have to lose... besides fat?</p>
<div class="btn-purple">Get my customized plan</div>

<footer class="footer">
  <h4 style="left:162px">About us</h4>
  <p class="about-text">Lorem Ipsum is simply dummy text of the printing and typesetting industry. Lorem Ipsum unknown printer text.</p>
  <div class="info" style="top:140px"><b><svg width="10" height="12" viewBox="0 0 10 12" fill="#fff"><path d="M5 12S0 7 0 4.5a5 5 0 0 1 10 0C10 7 5 12 5 12z"/></svg>ADDRESS:</b>1840 Harbour Crest Road, Tallowin Heads, 4230, Australia</div>
  <div class="info" style="top:210px"><b><svg width="10" height="12" viewBox="0 0 10 12" fill="#fff"><rect x="1" y="0" width="8" height="12" rx="1.5"/></svg>TELEPHONE:</b>0461538207</div>
  <div class="info" style="top:270px"><b><svg width="12" height="10" viewBox="0 0 12 10" fill="#fff"><rect width="12" height="10"/></svg>EMAIL:</b>info@brinovamotion.com</div>

  <h4 style="left:442px">Latest news</h4>
  <div class="news" style="top:87px">
    <div class="news-date"><strong>01</strong><span>JUN</span></div>
    <div class="news-more">Read More</div>
    <div class="news-body"><div class="t">Lorem Ipsum is simply dummy text</div><div class="m">07/11/2016 | 9:30 am - 12:00 pm<br>Morning Event Hall</div><div class="loc">Paris France</div></div>
  </div>
  <div class="news-line" style="top:163px"></div>
  <div class="news" style="top:174px">
    <div class="news-date"><strong>01</strong><span>JUN</span></div>
    <div class="news-more">Read More</div>
    <div class="news-body"><div class="t">Lorem Ipsum is simply dummy text</div><div class="m">07/11/2016 | 9:30 am - 12:00 pm<br>Morning Event Hall</div><div class="loc">Paris France</div></div>
  </div>
  <div class="news-line" style="top:250px"></div>
  <div class="news" style="top:262px">
    <div class="news-date"><strong>01</strong><span>JUN</span></div>
    <div class="news-body"><div class="t">Lorem Ipsum is simply dummy text</div><div class="m">07/11/2016 | 9:30 am - 12:00 pm<br>Morning Event Hall</div><div class="loc">Paris France</div></div>
  </div>

  <h4 style="left:755px">Book appointment</h4>
  <div class="form-field" style="top:87px">Enter your name</div>
  <div class="form-field" style="top:132px">Enter your email</div>
  <div class="form-field" style="top:174px;height:88px">Enter your message</div>
  <div class="btn-submit">SUBMIT</div>
</footer>
<div class="copyright">© 2018 brinovamotion.com. All rights reserved.</div>

</body>
</html>
```